Surface Protection company needs cards

We are a New Zealand company that will apply nanotechnology coatings on surfaces to prevent growth and spread of bacteria, viruses, mold etc with a sprayer. We deal with large corporates, airlines, hospitals and schools so we are after a new modern, simple and clean look that will have great visual impact.
We a company that is focused on prevention and protection.

Company name, Vela Shield

Subtext, Antimicrobial Surface Protection

Logo, VS

Target Market(s)

Hospitals, Transport agencies, Airlines, Corporate entities

Contact Information for Business Card

Company name, VelaShield
Logo, VS

Gareth Tolley
velashieldnz@postbox.example
+64219305562
www.velashield.example.nz

Requirements
Must have
• Simple clean look.
Nice to have
• We apply nano coatings so try and incorporate this into a theme somehow

```html
<!DOCTYPE html>
<html lang="en">
<head>
<meta charset="utf-8">
<title>Vela Shield – Business Cards</title>
<link rel="stylesheet" href="https://fonts.googleapis.com/css2?family=Raleway:wght@500;600&family=Roboto+Slab:wght@400&family=Arimo:wght@400&display=swap">
<style>
  :root {
    --backdrop: #d6d6d6;
    --brand-blue: #1467ad;
    --brand-green: #79a72a;
    --card-white: #efefef;
    --ink-dark: #2a2a2a;
    --text-light: #ffffff;
  }
  * { margin: 0; padding: 0; box-sizing: border-box; }
  html, body { width: 1200px; height: 802px; overflow: hidden; background: var(--backdrop); }
  .canvas { position: relative; width: 1200px; height: 802px; }
  .card { position: absolute; top: 274px; width: 443px; height: 265px; overflow: hidden; }
  .card-front { left: 136px; background: var(--brand-blue); color: var(--text-light); }
  .card-back { left: 624px; background: var(--card-white); }

  .accent-disc { position: absolute; left: -78px; top: 8px; width: 270px; height: 270px; border-radius: 50%; background: var(--brand-green); }

  .wordmark { position: absolute; font-family: "Raleway", sans-serif; font-weight: 500; white-space: nowrap; }
  .tagline { position: absolute; font-family: "Raleway", sans-serif; font-weight: 600; text-transform: uppercase; white-space: nowrap; }

  .card-front .wordmark { left: 236px; top: 48px; font-size: 30px; letter-spacing: 0.2px; }
  .card-front .tagline { left: 238px; top: 87px; font-size: 7px; letter-spacing: 0.6px; }
  .holder-name { position: absolute; left: 243px; top: 140px; font-family: "Roboto Slab", serif; font-size: 16.5px; }
  .contact-list { position: absolute; left: 243px; top: 186px; list-style: none; font-family: "Arimo", sans-serif; font-size: 11.5px; line-height: 17px; }
  .contact-list li { display: flex; align-items: center; gap: 5px; white-space: nowrap; }
  .contact-list svg { width: 13px; height: 13px; flex: none; }

  .droplet-texture { position: absolute; left: 0; top: 100px; width: 100%; height: 165px;
    background: linear-gradient(180deg, rgba(239,239,239,0) 0%, #e3e3e3 45%, #dcdcdc 100%); }
  .brand-dot { position: absolute; left: 193px; top: 66px; width: 56px; height: 56px; border-radius: 50%; background: var(--brand-blue); }
  .card-back .wordmark { left: 0; width: 100%; text-align: center; top: 136px; font-size: 36px; color: var(--brand-blue); }
  .card-back .tagline { left: 0; width: 100%; text-align: center; top: 185px; font-size: 9px; letter-spacing: 0.8px; color: var(--ink-dark); }
</style>
</head>
<body>
<main class="canvas">
  <section class="card card-front" aria-label="Business card front">
    <div class="accent-disc"></div>
    <div class="wordmark">Vela Shield</div>
    <div class="tagline">Antimicrobial Surface Protection</div>
    <div class="holder-name">Gareth Tolley</div>
    <ul class="contact-list">
      <li>
        <svg viewBox="0 0 14 14" aria-hidden="true"><rect x="0.7" y="0.7" width="12.6" height="12.6" rx="2" fill="none" stroke="#fff" stroke-width="1.2"/><path d="M4.3 3.2c.6 0 1.2 1.3 1.2 1.7s-.8.7-.6 1.2c.4.9 1.2 1.8 2.2 2.3.4.2.7-.6 1.1-.6s1.7.6 1.7 1.2-.7 1.4-1.5 1.4C5.8 10.4 3.4 7.9 3.2 5c0-.9.5-1.8 1.1-1.8z" fill="#fff"/></svg>
        <span>+64219305562</span>
      </li>
      <li>
        <svg viewBox="0 0 14 14" aria-hidden="true"><rect x="0.5" y="2.5" width="13" height="9" fill="#fff"/><path d="M0.5 2.5 7 8l6.5-5.5M0.5 11.5 5.3 6.7M13.5 11.5 8.7 6.7" fill="none" stroke="#1467ad" stroke-width="1"/></svg>
        <span>velashieldnz@postbox.example</span>
      </li>
      <li>
        <svg viewBox="0 0 14 14" aria-hidden="true"><g fill="none" stroke="#fff" stroke-width="1.1"><circle cx="7" cy="7" r="6.2"/><ellipse cx="7" cy="7" rx="2.7" ry="6.2"/><path d="M0.8 7h12.4M1.8 4h10.4M1.8 10h10.4"/></g></svg>
        <span>www.velashield.example.nz</span>
      </li>
    </ul>
  </section>

  <section class="card card-back" aria-label="Business card back">
    <div class="droplet-texture" role="img" aria-label="Texture of water droplets beading on a coated surface"></div>
    <div class="brand-dot"></div>
    <div class="wordmark">Vela Shield</div>
    <div class="tagline">Antimicrobial Surface Protection</div>
  </section>
</main>
</body>
</html>
```